New Infusion Pharmacy needs Business Card design

Hello!

We are Verant Infusion Pharmacy, are we are looking for a two sided, clean and modern business card.

First, let me give you a little bit about what an infusion pharmacy does...
We compound and fill prescriptions for drugs that are injectable, meaning that they are administered via an IV bag or a syringe. Basically anything that is too advanced for a normal pill pharmacy to fill. We compound everything in our state of the art clean room, then deliver it directly to the patients home. We have an outside sales force that markets to hospitals, home health agencies, and doctor's offices.

as for the business card...
We are looking for a clean, modern card. our colors are in our logo, kind of a light bule and a darker blue. We do really like the rounded corners on the card. Also, we would like the back of the card to be the reverse colors of the front, for example, if the front of the card has a light background, then the back of the card will have a dark background.

On the back side of the card we want to have our logo, then list some of the services we offer:
-IVIG
-TPN
-Enteral Nutrition
-IV Antibiotics
-IV Hydration
-Blood Factors
-Chemotherapy
-Pain Management

Our logo is uploaded in .psd format, if you need a different format let me know and i'll throw it up here.

Thank you so much!!

Industry/Entity Type

Pharmacy

Requirements
Must have
• Front of Card: (no particular order, please arrange in whatever way you think looks best!)
-Employee Name
-Title
-Office Phone #
-Cell Phone #
-Fax #
-email address - marlo@verantcareinfuse.com
-office address - 4127 Delmore St. Larkfield, CA 94312
-Web Site - www.verantcareinfuse.com

```html
<!DOCTYPE html>
<html lang="en">
<head>
<meta charset="utf-8">
<title>Verant Infusion Pharmacy – Business Card</title>
<link rel="stylesheet" href="https://fonts.googleapis.com/css2?family=Questrial&display=swap">
<style>
  :root {
    --backdrop: #4a3228;
    --navy: #15557a;
    --navy-light: #2f6a92;
    --brand-blue: #2fa4c9;
    --panel-top: #3a9fc2;
    --panel-bottom: #2a86ab;
    --ink-white: #f2f7fa;
    --ink-navy: #1a5676;
    --paper-light: #ffffff;
    --paper-edge: #d3d3d3;
  }
  * { margin: 0; padding: 0; box-sizing: border-box; }
  html, body { width: 1200px; height: 1181px; overflow: hidden; }
  body {
    background: var(--backdrop);
    font-family: "Questrial", sans-serif;
    position: relative;
  }
  .card {
    position: absolute;
    top: 199px;
    width: 446px;
    height: 773px;
    border-radius: 30px;
    overflow: hidden;
    box-shadow: 0 6px 18px rgba(0,0,0,0.45);
  }
  .card--services {
    left: 116px;
    background: radial-gradient(ellipse 70% 55% at 50% 48%, var(--navy-light) 0%, var(--navy) 100%);
  }
  .card--contact {
    left: 626px;
    background: radial-gradient(ellipse 65% 50% at 50% 55%, var(--paper-light) 0%, var(--paper-edge) 100%);
    color: var(--ink-navy);
    text-align: center;
    word-spacing: 4px;
  }
  .brand-name {
    position: absolute;
    top: 78px;
    left: 0;
    width: 100%;
    text-align: center;
    color: var(--brand-blue);
    font-size: 30px;
    letter-spacing: 1px;
  }
  .services-heading {
    position: absolute;
    top: 436px;
    width: 100%;
    text-align: center;
    color: var(--ink-white);
    font-size: 19px;
    word-spacing: 5px;
  }
  .services-panel {
    position: absolute;
    left: 86px;
    top: 477px;
    width: 275px;
    height: 239px;
    border-radius: 26px;
    background: linear-gradient(180deg, var(--panel-top), var(--panel-bottom));
    box-shadow: 0 3px 8px rgba(0,0,0,0.3);
    padding: 21px 0 0 30px;
    list-style: none;
  }
  .services-panel li {
    color: var(--ink-white);
    font-size: 19px;
    line-height: 24.2px;
    word-spacing: 4px;
  }
  .services-panel li::before { content: "- "; font-weight: bold; margin-right: 3px; word-spacing: 0; }
  .accent-band {
    position: absolute;
    left: 69px;
    width: 307px;
    height: 11px;
    background: var(--ink-navy);
  }
  .accent-band--top { top: 0; }
  .accent-band--bottom { bottom: 0; }
  .employee-name {
    position: absolute;
    top: 346px;
    width: 100%;
    font-size: 32px;
    letter-spacing: 0.5px;
    word-spacing: 6px;
  }
  .employee-title {
    position: absolute;
    top: 385px;
    width: 100%;
    font-size: 24px;
    word-spacing: 5px;
  }
  .contact-lines {
    position: absolute;
    top: 622px;
    width: 100%;
    font-size: 19px;
    line-height: 21.6px;
    list-style: none;
  }
</style>
</head>
<body>
  <section class="card card--services">
    <div class="brand-name">Verant Infusion Pharmacy</div>
    <p class="services-heading">Services we offer</p>
    <ul class="services-panel">
      <li>IVIG</li>
      <li>TPN</li>
      <li>Enteral Nutrition</li>
      <li>IV Antibiotics</li>
      <li>IV Hydration</li>
      <li>Blood Factors</li>
      <li>Chemotherapy</li>
      <li>Pain Management</li>
    </ul>
  </section>

  <section class="card card--contact">
    <div class="accent-band accent-band--top"></div>
    <p class="employee-name">Name Of Employee</p>
    <p class="employee-title">title of employee</p>
    <ul class="contact-lines">
      <li>Office Phone #</li>
      <li>Cell Phone #</li>
      <li>Fax #</li>
      <li>marlo@verantcareinfuse.com</li>
      <li>4127 Delmore St. Larkfield, CA 94312</li>
      <li>www.verantcareinfuse.com</li>
    </ul>
    <div class="accent-band accent-band--bottom"></div>
  </section>
</body>
</html>
```